Corporate Hollowmere business cards to be handed to investor, bankers etc. Needs to have a young feel

I need business cards designed for a technology company that provides vanto-like rapid response on the security industry. I would like it simple but very cool and tasteful. See attached documents for artwork and colours to be used. Cut sheet describes business model. Card stock should be thicker than normal. I would like the one side to be just the art and the other to have the contact info with maybe the pin somewhere.

Target Market(s)

Investors

Industry/Entity Type

Business

Contact Information for Business Card

Would like the logo attached on one side with name address and other info on the other side.

Font styles to use
Other font styles liked:
• See existing logo

Colors
6b449b
886aae
e4daeb
ffffff

Requirements
Must have
• Name: Gregory Thalassides
• Address: 47 Orchard Lane, Toronto, On, L6R2C8
• Tel: 647-5550192
• Email: greg@hollowmere.io
Nice to have
• See logo colours

```html
<!DOCTYPE html>
<html lang="en">
<head>
<meta charset="utf-8">
<title>Hollowmere Business Cards</title>
<link rel="stylesheet" href="https://fonts.googleapis.com/css2?family=Lato:wght@400&family=Oswald:wght@600&display=swap">
<style>
  :root {
    --backdrop: #3b4049;
    --card: #2b2b2d;
    --card-edge: #1f1f21;
    --purple: #6b449b;
    --purple-light: #886aae;
    --lilac: #e4daeb;
    --white: #ffffff;
  }
  * { box-sizing: border-box; margin: 0; padding: 0; }
  html, body {
    width: 1200px;
    height: 900px;
    overflow: hidden;
    background: var(--backdrop);
  }
  .sheet {
    width: 1200px;
    height: 900px;
    display: flex;
    flex-direction: column;
    align-items: center;
    justify-content: center;
    gap: 60px;
  }
  .card {
    width: 630px;
    height: 360px;
    background: linear-gradient(160deg, #333335 0%, var(--card) 55%, #252527 100%);
    border-radius: 4px;
    box-shadow: 0 2px 0 var(--card-edge), 0 14px 30px rgba(0,0,0,0.35);
    position: relative;
  }
  /* Front */
  .card--front {
    display: flex;
    align-items: center;
    justify-content: center;
  }
  .company-name {
    font-family: "Lato", sans-serif;
    font-weight: 400;
    font-size: 60px;
    color: var(--white);
    line-height: 1;
  }
  /* Back */
  .card--back {
    display: flex;
    align-items: center;
    justify-content: center;
    gap: 34px;
  }
  .holder {
    font-family: "Oswald", sans-serif;
    font-weight: 600;
    font-size: 40px;
    line-height: 1.05;
    text-transform: uppercase;
    color: var(--purple-light);
    text-align: right;
  }
  .divider {
    width: 2px;
    height: 130px;
    background: var(--purple);
  }
  .contact {
    list-style: none;
    font-family: "Lato", sans-serif;
    font-weight: 400;
    font-size: 21px;
    line-height: 1.35;
    color: var(--white);
  }
  .contact__line {
    position: relative;
  }
  .contact__icon {
    position: absolute;
    left: -26px;
    top: 6px;
    width: 16px;
    height: 16px;
  }
</style>
</head>
<body>
<main class="sheet">
  <section class="card card--front" aria-label="Card front">
    <p class="company-name">Hollowmere</p>
  </section>

  <section class="card card--back" aria-label="Card back">
    <h1 class="holder">Gregory<br>Thalassides</h1>
    <span class="divider"></span>
    <ul class="contact">
      <li class="contact__line">47 Orchard Lane</li>
      <li class="contact__line">Toronto, On, L6R2C8</li>
      <li class="contact__line">
        <svg class="contact__icon" viewBox="0 0 24 24" aria-hidden="true">
          <path fill="#886aae" d="M6.6 10.8a15.1 15.1 0 0 0 6.6 6.6l2.2-2.2a1 1 0 0 1 1-.25 11.4 11.4 0 0 0 3.6.57 1 1 0 0 1 1 1V20a1 1 0 0 1-1 1A17 17 0 0 1 3 4a1 1 0 0 1 1-1h3.5a1 1 0 0 1 1 1c0 1.250.2 2.450.57 3.570a1 1 0 0 1-.25 1z"/>
        </svg>647-5550192
      </li>
      <li class="contact__line">
        <svg class="contact__icon" viewBox="0 0 24 24" aria-hidden="true">
          <rect x="2" y="5" width="20" height="14" rx="1.5" fill="#886aae"/>
          <path d="M3 6l9 7 9-7" fill="none" stroke="#2b2b2d" stroke-width="1.8"/>
        </svg>greg@hollowmere.io
      </li>
    </ul>
  </section>
</main>
</body>
</html>
```